Cosmetic Surgery Ad for a magazine

We would like design options for our cosmetic surgery practice located in California for summer advertizing breast augmentation and liposuction to get ready for a beach body.

Target Market(s)

Women ages 25 - 40

Industry/Entity Type

Cosmetic

Other font styles liked:
• see brand standards attachment

Requirements
Must have
• Our logo (see brand standards attachment)
Should not have
• Nudity

```html
<!DOCTYPE html>
<html lang="en">
<head>
<meta charset="utf-8">
<title>Best Body This Summer – Lumorelle Cosmetic Surgery and Medspa</title>
<link rel="stylesheet" href="https://fonts.googleapis.com/css2?family=Roboto+Condensed:wght@700&display=swap">
<style>
  :root {
    --sky-top: #5fc3c0;
    --sea-mid: #9fd6b8;
    --sea-low: #cfe3a6;
    --sand-warm: #d9c98f;
    --headline: rgba(255, 255, 255, 0.86);
    --with-text: #fbe9ee;
    --brand-green: #5ee35c;
    --brand-pink: #cf8fe6;
    --tagline-purple: #8a3fb0;
  }
  html, body {
    margin: 0;
    padding: 0;
    width: 927px;
    height: 1200px;
    overflow: hidden;
    background: #ffffff;
  }
  .ad {
    position: relative;
    width: 927px;
    height: 1200px;
    overflow: hidden;
  }
  .beach-photo {
    position: absolute;
    inset: 0;
    background:
      radial-gradient(ellipse 38% 60% at 50% 48%, rgba(214, 160, 120, 0.55), rgba(214, 160, 120, 0) 70%),
      linear-gradient(180deg, var(--sky-top) 0%, var(--sky-top) 8%, var(--sea-mid) 30%, var(--sea-low) 70%, var(--sand-warm) 100%);
  }
  .ad-type {
    position: absolute;
    inset: 0;
    width: 927px;
    height: 1200px;
    font-family: "Roboto Condensed", "Arial Narrow", sans-serif;
    font-weight: 700;
  }
  .headline { fill: var(--headline); }
  .with-line { fill: var(--with-text); }
  .brand-name { fill: var(--brand-green); }
  .brand-dot { fill: var(--brand-pink); }
  .brand-tagline { fill: var(--tagline-purple); }
</style>
</head>
<body>
  <main class="ad">
    <div class="beach-photo" role="img" aria-label="Sunlit photo of a smiling woman in a black bikini and sunglasses standing in shallow turquoise sea, arms raised behind her head"></div>

    <svg class="ad-type" viewBox="0 0 927 1200" xmlns="http://www.w3.org/2000/svg" aria-label="Get your best body this summer with Lumorelle Cosmetic Surgery and Medspa">
      <text class="headline" x="129" y="257" font-size="176" textLength="666" lengthAdjust="spacingAndGlyphs">GET YOUR</text>
      <text class="headline" x="129" y="536" font-size="338" textLength="669" lengthAdjust="spacingAndGlyphs">BEST</text>
      <text class="headline" x="129" y="798" font-size="338" textLength="669" lengthAdjust="spacingAndGlyphs">BODY</text>
      <text class="headline" x="144" y="917" font-size="128" textLength="654" lengthAdjust="spacingAndGlyphs">THIS SUMMER!</text>

      <text class="with-line" x="420" y="1015" font-size="48" textLength="90" lengthAdjust="spacingAndGlyphs">with</text>

      <circle class="brand-dot" cx="630" cy="990" r="26"/>
      <text class="brand-name" x="276" y="1084" font-size="86" textLength="392" lengthAdjust="spacingAndGlyphs">Lumorelle</text>
      <text class="brand-tagline" x="280" y="1108" font-size="17" textLength="276" lengthAdjust="spacingAndGlyphs">COSMETIC SURGERY AND MEDSPA</text>
    </svg>
  </main>
</body>
</html>
```